Belmorin InsurTech Website Redesign - 10 Pages

Design a modern, professional website for Belmorin, an AI-native cyber insurance platform serving SMBs.

DELIVERABLE: 10 pages (desktop + mobile mockups)
- Homepage (priority #1)
- 4 Platform pages (Cyber Insurance, Brokers, Underwriters, Policyholder)
- 3 Company pages (About Us, Team, Contact/Careers)
- 2 Risk pages (AI Risk, Cyber Risk)

DESIGN DIRECTION:
- Professional + innovative (insurance meets technology)
- Trust-building + modern aesthetic
- Reference: Pellbrook Insurance, Driftmoor Insurance
- Use official brand colors (6-color palette provided)
- Avoid generic security clipart (padlocks, shields, magnifying glasses)
- Custom graphics, not AI-generated or stock imagery

CURRENT SITES FOR REFERENCE:
- www.belmorin-cover.test
- https://a3c9140d.belmorin-website.previewhost.test/

Full detailed brief with all content, page specifications, and brand guidelines attached as PDF (Belmorin_MockupLane_Brief.pdf).

TARGET AUDIENCE: Insurance brokers (primary), SMB business owners (secondary)
KEY MESSAGE: "Cyber Insurance the Way It Should Be"

Additional brand assets available in Google Drive - link provided on request.

```html
<!DOCTYPE html>
<html lang="en">
<head>
<meta charset="utf-8">
<title>Belmorin – Home</title>
<link rel="stylesheet" href="https://fonts.googleapis.com/css2?family=Arimo:wght@400;700&display=swap">
<style>
  :root {
    --page-navy: #1b2652;
    --page-navy-deep: #16204a;
    --nav-bg: #141c3e;
    --nav-line: #222c55;
    --white: #ffffff;
    --muted-text: #d8dce4;
    --accent-teal: #63d2cc;
    --button-text: #15203f;
    --label-yellow: #f3e90c;
    --hero-green: #00d27c;
    --hero-teal: #12c6a2;
    --hero-edge: #d8262a;
  }
  * { box-sizing: border-box; margin: 0; padding: 0; }
  html, body {
    width: 1200px;
    height: 644px;
    overflow: hidden;
  }
  body {
    font-family: "Arimo", Arial, sans-serif;
    background: linear-gradient(180deg, var(--page-navy-deep) 0%, var(--page-navy) 60%, var(--page-navy-deep) 100%);
    position: relative;
    color: var(--white);
  }
  .site-nav {
    position: absolute;
    left: 0; top: 0;
    width: 1200px;
    height: 55px;
    background: var(--nav-bg);
    border-bottom: 1px solid var(--nav-line);
  }
  .brand-name {
    position: absolute;
    left: 102px;
    top: 16px;
    font-size: 18px;
    font-weight: 700;
    color: var(--white);
  }
  .nav-links {
    position: absolute;
    top: 20px;
    list-style: none;
    font-size: 11px;
    color: var(--white);
  }
  .nav-links li {
    position: absolute;
    white-space: nowrap;
  }
  .nav-caret {
    display: inline-block;
    margin-left: 5px;
    width: 0; height: 0;
    border-left: 2.5px solid transparent;
    border-right: 2.5px solid transparent;
    border-top: 3px solid var(--white);
    vertical-align: middle;
  }
  .demo-button {
    position: absolute;
    left: 944px;
    top: 13px;
    width: 108px;
    height: 27px;
    border-radius: 3px;
    background: var(--accent-teal);
    color: var(--white);
    font-size: 11px;
    font-weight: 700;
    text-align: center;
    line-height: 27px;
  }
  .screen-label {
    position: absolute;
    left: 19px;
    top: 85px;
    font-size: 21px;
    font-weight: 700;
    color: var(--label-yellow);
  }
  .hero {
    position: absolute;
    left: 142px;
    top: 118px;
    width: 872px;
    height: 460px;
    border: 1px solid var(--hero-edge);
    border-radius: 3px;
    overflow: hidden;
  }
  .hero-art {
    position: absolute;
    inset: 0;
    background: linear-gradient(160deg, var(--hero-green) 0%, var(--hero-teal) 50%, var(--hero-green) 100%);
  }
  .hero-content {
    position: absolute;
    left: 16px;
    top: 0;
    right: 0;
    bottom: 0;
  }
  .hero-title {
    position: absolute;
    left: 0;
    top: 160px;
    font-size: 35px;
    font-weight: 700;
    color: var(--white);
    white-space: nowrap;
  }
  .hero-subtitle {
    position: absolute;
    left: 0;
    top: 228px;
    font-size: 27px;
    font-weight: 400;
    color: var(--muted-text);
    white-space: nowrap;
  }
  .contact-button {
    position: absolute;
    left: 0;
    top: 282px;
    width: 95px;
    height: 29px;
    border-radius: 3px;
    background: var(--accent-teal);
    color: var(--button-text);
    font-size: 12px;
    font-weight: 700;
    text-align: center;
    line-height: 29px;
  }
</style>
</head>
<body>
  <header class="site-nav">
    <div class="brand-name">Belmorin</div>
    <ul class="nav-links">
      <li style="left:635px">Platform<span class="nav-caret"></span></li>
      <li style="left:712px">Cyber Risk</li>
      <li style="left:789px">AI Risk</li>
      <li style="left:846px">Company<span class="nav-caret"></span></li>
    </ul>
    <div class="demo-button">Request Demo</div>
  </header>

  <div class="screen-label">Screen-1 : index.php</div>

  <section class="hero">
    <div class="hero-art" role="img" aria-label="Hero illustration: abstract geometric artwork in green, red, blue and yellow"></div>
    <div class="hero-content">
      <h1 class="hero-title">Cyber Insurance the Way It Should Be</h1>
      <p class="hero-subtitle">Evidence-based, automation-driven underwriting for the AI era.</p>
      <div class="contact-button">Contact Us</div>
    </div>
  </section>
</body>
</html>
```